Single brochure for international companies in the financial sector

We need to update a brochure 4 pages presenting our company. We are a financial engineering company. The final design must provide financial security, service and trust. you will find the current brochure copy. Our color code is Orange (RGB 235/100/68), Black, White and Gray. photos show the visual of the site, but it is not mandatory to keep them.

Target Market(s)

wealth management professionals

Industry/Entity Type

Finance

Requirements
Must have
• Logo Tolvane Capital all text in the document color Orange Tolvane (RGB 235/100/68)
Nice to have
• Vista Font
Should not have
• images / pictures of people

```html
<!DOCTYPE html>
<html lang="en">
<head>
<meta charset="utf-8">
<title>Tolvane Capital — Brochure Cover</title>
<link rel="stylesheet" href="https://fonts.googleapis.com/css2?family=Questrial&display=swap">
<style>
  :root {
    --orange: rgb(235, 100, 68);
    --black: #1a1a1a;
    --white: #ffffff;
    --gray: #c9c9c9;
    --stone-light: #e4e4e4;
    --stone-dark: #5a5a5a;
  }
  * { margin: 0; padding: 0; box-sizing: border-box; }
  html, body {
    width: 1200px; height: 847px; overflow: hidden;
    background: var(--gray);
    font-family: "Questrial", sans-serif;
  }
  .spread {
    position: absolute; left: 80px; top: 55px;
    width: 1040px; height: 736px;
    display: flex;
    box-shadow: 0 12px 30px rgba(0,0,0,0.25);
  }
  .page { position: relative; width: 520px; height: 736px; overflow: hidden; }

  /* Back cover */
  .back-cover { background: var(--orange); color: var(--white); }
  .wordmark { position: absolute; left: 0; width: 100%; text-align: center; }
  .wordmark .name { display: block; font-size: 26px; letter-spacing: 0.75em; padding-left: 0.75em; }
  .wordmark .sub { display: block; font-size: 15px; letter-spacing: 0.55em; padding-left: 0.55em; margin-top: 6px; }
  .back-cover .wordmark { top: 300px; }

  .contact-card {
    position: absolute; left: 170px; top: 470px;
    width: 220px; height: 266px;
    background: var(--white); color: var(--black);
    text-align: center; font-size: 11.5px; line-height: 1.35;
    padding-top: 24px;
  }
  .contact-item { margin-bottom: 10px; }
  .contact-icon { display: block; margin: 0 auto 3px; width: 13px; height: 13px; }
  .social-row { display: flex; justify-content: center; gap: 6px; margin-top: 14px; }
  .social-square { width: 16px; height: 16px; background: var(--black); border-radius: 2px; }

  /* Front cover */
  .front-cover { background: var(--white); }
  .front-cover .wordmark { top: 56px; left: 40px; width: 300px; color: var(--black); }
  .cover-photo { position: absolute; inset: 0; width: 520px; height: 736px; }
  .title-box {
    position: absolute; left: 320px; top: 430px;
    width: 190px; height: 250px;
    background: var(--orange); color: var(--white);
  }
  .title-box h1 {
    position: absolute; left: 20px; top: 48px;
    font-weight: 400; font-size: 21px; line-height: 1.15; letter-spacing: 0.01em;
  }
  .title-box .url { position: absolute; left: 0; bottom: 16px; width: 100%; text-align: center; font-size: 10px; }
</style>
</head>
<body>
  <main class="spread">
    <section class="page back-cover">
      <div class="wordmark">
        <span class="name">TOLVANE</span>
        <span class="sub">CAPITAL</span>
      </div>
      <div class="contact-card">
        <div class="contact-item">
          <svg class="contact-icon" viewBox="0 0 14 14"><circle cx="7" cy="7" r="6.3" fill="none" stroke="#1a1a1a"/><path d="M7 3.2a2.3 2.3 0 0 0-2.3 2.3C4.7 7.3 7 10.5 7 10.5s2.3-3.2 2.3-5A2.3 2.3 0 0 0 7 3.2z" fill="#1a1a1a"/></svg>
          Tolvane Capital SA, 14 rue<br>Verlaine 75008 PARIS
        </div>
        <div class="contact-item">
          <svg class="contact-icon" viewBox="0 0 14 14"><circle cx="7" cy="7" r="6.3" fill="none" stroke="#1a1a1a"/><path d="M4.5 4c.6-.5 1.1-.3 1.4.3l.4.9c.2.4 0 .7-.3.9.4.9 1 1.5 1.9 1.9.2-.3.5-.5.9-.3l.9.4c.6.3.8.8.3 1.4-1.6 1.4-6.8-3.9-5.5-5.5z" fill="#1a1a1a"/></svg>
          +33 1 40 27 18 55
        </div>
        <div class="contact-item">
          <svg class="contact-icon" viewBox="0 0 14 14"><circle cx="7" cy="7" r="6.3" fill="none" stroke="#1a1a1a"/><circle cx="7" cy="7" r="3.5" fill="none" stroke="#1a1a1a" stroke-width="0.8"/><path d="M3.5 7h7M7 3.5v7" stroke="#1a1a1a" stroke-width="0.8"/></svg>
          www.tolvanecapital.com
        </div>
        <div class="contact-item">
          <svg class="contact-icon" viewBox="0 0 14 14"><circle cx="7" cy="7" r="6.3" fill="none" stroke="#1a1a1a"/><rect x="3.8" y="4.8" width="6.4" height="4.4" fill="#1a1a1a"/><path d="M3.8 4.8 7 7.3l3.2-2.5" stroke="#fff" stroke-width="0.7" fill="none"/></svg>
          contact@tolvanecapital.com
        </div>
        <div class="social-row">
          <span class="social-square"></span>
          <span class="social-square"></span>
          <span class="social-square"></span>
          <span class="social-square"></span>
        </div>
      </div>
    </section>

    <section class="page front-cover">
      <svg class="cover-photo" viewBox="0 0 520 736" role="img" aria-label="Black and white photograph of an old stone arched bridge rising diagonally toward the top right">
        <defs>
          <linearGradient id="stone" x1="0" y1="1" x2="1" y2="0">
            <stop offset="0" stop-color="var(--stone-dark)"/>
            <stop offset="0.55" stop-color="#9a9a9a"/>
            <stop offset="1" stop-color="var(--stone-light)"/>
          </linearGradient>
        </defs>
        <polygon points="0,520 90,470 520,0 520,736 0,736" fill="url(#stone)"/>
      </svg>
      <div class="wordmark">
        <span class="name">TOLVANE</span>
        <span class="sub">CAPITAL</span>
      </div>
      <div class="title-box">
        <h1>FINANCIAL<br>ENGINEERING</h1>
        <span class="url">www.tolvanecapital.com</span>
      </div>
    </section>
  </main>
</body>
</html>
```